Print and E-book Personal Injury Front and Back Book Cover

I need a book cover for a personal injury law firm book titled "Rising Past the Wreckage" with the subtitle "A Plain Guide for Harmed Readers." The book cover should have an image. This isas a lead generation book designed to be give to potential clients to have them sign as new clients.

Target Market(s)

Potential New Clients Looking For a Personal Injury Attorney

Industry/Entity Type

Legal

Requirements
Must have
• Title and some type of image or images

```html
<!DOCTYPE html>
<html lang="en">
<head>
<meta charset="utf-8">
<title>Rising Past the Wreckage — Book Cover</title>
<link rel="stylesheet" href="https://fonts.googleapis.com/css2?family=Cinzel:wght@500;700&family=Montserrat:wght@600&display=swap">
<style>
  :root {
    --paper: #ffffff;
    --rust: #b0532a;
    --copper: #9a4a22;
    --band: #7b3a20;
    --band-text: #ffffff;
    --photo-light: #f2f1ef;
    --photo-mid: #dcdad6;
  }
  html, body {
    margin: 0;
    padding: 0;
    overflow: hidden;
    background: var(--paper);
  }
  .cover {
    position: relative;
    width: 750px;
    height: 1200px;
    background: var(--paper);
    overflow: hidden;
  }
  .title-line {
    position: absolute;
    left: 0;
    width: 100%;
    margin: 0;
    text-align: center;
    line-height: 1;
    font-family: "Cinzel", serif;
    text-transform: uppercase;
  }
  .title-line--small {
    font-size: 52px;
    font-weight: 500;
    color: var(--rust);
    letter-spacing: 1px;
  }
  .title-line--large {
    font-size: 104px;
    font-weight: 700;
    color: var(--copper);
  }
  .line-1 { top: 92px; }
  .line-2 { top: 150px; }
  .line-3 { top: 272px; }
  .line-4 { top: 328px; }

  .emblem {
    position: absolute;
    left: 135px;
    top: 508px;
    width: 480px;
    height: 480px;
  }
  .subtitle-band {
    position: absolute;
    left: 0;
    bottom: 0;
    width: 100%;
    height: 82px;
    background: var(--band);
    display: flex;
    align-items: center;
    justify-content: center;
  }
  .subtitle {
    margin: 0;
    font-family: "Montserrat", sans-serif;
    font-weight: 600;
    font-size: 22px;
    letter-spacing: 2px;
    text-transform: uppercase;
    color: var(--band-text);
  }
</style>
</head>
<body>
  <main class="cover">
    <h1 class="book-title">
      <span class="title-line title-line--small line-1">Rising</span>
      <span class="title-line title-line--large line-2">Past</span>
      <span class="title-line title-line--small line-3">the</span>
      <span class="title-line title-line--large line-4">Wreckage</span>
    </h1>

    <svg class="emblem" viewBox="0 0 480 480" aria-hidden="false">
      <defs>
        <radialGradient id="marble" cx="45%" cy="40%" r="65%">
          <stop offset="0%" stop-color="var(--photo-light)"/>
          <stop offset="100%" stop-color="var(--photo-mid)"/>
        </radialGradient>
      </defs>
      <circle cx="240" cy="240" r="236" fill="none" stroke="var(--copper)" stroke-width="7"/>
      <circle cx="240" cy="240" r="222" fill="url(#marble)" role="img"
              aria-label="Photo of a wooden judge's gavel and sound block on a white marble surface"/>
    </svg>

    <footer class="subtitle-band">
      <p class="subtitle">A Plain Guide for Harmed Readers.</p>
    </footer>
  </main>
</body>
</html>
```